Venlox - Property Management Company Listings - PSD / uncoded only

Our site simply connects property owners with property managers. I’m asking you to create 2 pages, 1 homepage and 1 page that lists of property management companies. Build with Responsive Design in mind. PSD/uncoded files only. Help us create a great site!
Example competitor sites:
http://www.everyestatehelp.example/
http://www.tendyourlots.example/
Inspired by these sites:
http://www.quorvik.example/
http://www.bespokely.example/
http://www.coinwire.example/
https://www.tripboard.example/
I've attached the logo as well as 2 picture files that you can consider using.
• Venlox Logo Colors: Yellow: HTML code: #FBC30A, RGB code: R: 251 G: 195 B: 10 Grey: HTML code: #4E4C4D, RGB code: R: 78 G: 76 B: 77
• The picture files are optional.
o One picture is of houses and neighborhood.
o The other is of a professional woman on the phone. Please do not use the professional woman as a large primary image. You can use the professional woman photo as a smaller photo and not the main photo.
• Please bring your own pictures and graphics too. Don't feel like you need to use mine.
Thank you!

```html
<!DOCTYPE html>
<html lang="en">
<head>
<meta charset="utf-8">
<title>Venlox – Find Your Local Property Manager</title>
<link rel="stylesheet" href="https://fonts.googleapis.com/css2?family=Lato:wght@400;700&display=swap">
<style>
:root{
  --yellow:#fbc30a;
  --yellow-panel:rgba(250,198,10,.93);
  --grey:#4e4c4d;
  --dark:#3b3b3b;
  --text:#555;
  --light:#f0f0f0;
  --white:#fff;
}
*{box-sizing:border-box;margin:0;padding:0}
html,body{width:1200px;height:1156px;overflow:hidden}
body{font-family:'Lato',sans-serif;color:var(--grey);background:var(--white);position:relative}
.site-header{position:absolute;top:0;left:0;width:1200px;height:111px;background:var(--white)}
.brand{position:absolute;left:34px;top:30px;display:flex;align-items:center;gap:10px}
.brand-mark{width:26px;height:26px;background:var(--yellow)}
.brand-name{font-size:52px;font-weight:700;color:var(--grey);line-height:1;letter-spacing:-1px}
.expert-line{position:absolute;right:34px;top:5px;font-size:14px;color:var(--grey);display:flex;align-items:center;gap:12px}
.main-nav{position:absolute;top:55px;right:37px;display:flex;gap:58px}
.nav-item{display:flex;flex-direction:column;align-items:center;gap:6px;font-size:17px;font-weight:700;color:var(--grey);text-decoration:none}
.nav-item svg{height:20px}
.hero{position:absolute;top:111px;left:0;width:1200px;height:400px;
  background:linear-gradient(180deg,#b9b3ac 0%,#9c8e84 35%,#8d6f5e 65%,#7a6352 100%)}
.finder{position:absolute;left:227px;top:22px;width:747px;height:217px;background:var(--yellow-panel);color:var(--grey)}
.finder h1{position:absolute;top:22px;width:100%;text-align:center;font-size:24px;font-weight:700}
.field-label{position:absolute;top:76px;font-size:15px}
.select{position:absolute;left:31px;top:100px;width:386px;height:36px;background:var(--white);border:1px solid #bbb;font-size:15px;color:#888;padding:8px 12px}
.select-btn{position:absolute;right:-1px;top:-1px;width:37px;height:36px;background:var(--dark);display:flex;align-items:center;justify-content:center}
.zip{position:absolute;left:457px;top:100px;width:111px;height:36px;background:var(--white);border:1px solid #bbb}
.search-btn{position:absolute;left:608px;top:100px;width:111px;height:36px;background:var(--dark);color:var(--white);font-size:16px;display:flex;align-items:center;justify-content:center;gap:10px}
.finder p{position:absolute;top:158px;left:40px;right:40px;text-align:center;font-size:15px;line-height:17px}
.steps-title{position:absolute;top:538px;width:1200px;text-align:center;font-size:22px;font-weight:700;color:#555}
.step{position:absolute;top:626px;width:340px;text-align:center;font-size:17px;color:var(--text);line-height:18px}
.step svg{display:block;margin:0 auto 32px;height:72px}
.info-box{position:absolute;top:836px;width:528px;height:220px;border:2px solid var(--grey);background:var(--light)}
.info-box h2{font-size:26px;font-weight:400;text-align:center;color:var(--grey);margin-top:22px}
.info-box p{font-size:15px;line-height:26px;color:var(--text);padding:0 20px;margin-top:26px}
.learn-btn{display:block;width:154px;height:48px;margin:19px auto 0 179px;background:var(--yellow);border:1px solid #a47f00;border-radius:3px;font-size:21px;color:var(--grey);text-align:center;line-height:46px}
.reasons{list-style:none;margin-top:30px;padding-left:22px}
.reasons li{display:flex;align-items:center;gap:16px;font-size:15px;color:var(--text);height:44px}
.site-footer{position:absolute;top:1100px;left:0;width:1200px;height:56px;background:var(--grey);color:var(--white);font-size:14px;display:flex;align-items:center;justify-content:space-between;padding:0 23px 0 25px}
.footer-links a{color:var(--white);text-decoration:none}
.footer-links span{margin:0 6px}
</style>
</head>
<body>
<header class="site-header">
  <div class="brand"><span class="brand-mark"></span><span class="brand-name">venlox</span></div>
  <div class="expert-line">TALK TO EXPERT
    <svg width="14" height="14" viewBox="0 0 14 14"><circle cx="7" cy="4" r="3.3" fill="#4e4c4d"/><path d="M1 14c0-4 3-6 6-6s6 2 6 6z" fill="#4e4c4d"/></svg>
    555-014-2290</div>
  <nav class="main-nav">
    <a class="nav-item" href="#"><svg viewBox="0 0 20 18" width="20"><path d="M10 1 1 9h3v8h5v-5h2v5h5V9h3z" fill="#4e4c4d"/></svg>Home</a>
    <a class="nav-item" href="#"><svg viewBox="0 0 14 20" width="14"><circle cx="7" cy="7" r="5" fill="none" stroke="#4e4c4d" stroke-width="2"/><rect x="5" y="13" width="4" height="4" fill="#4e4c4d"/></svg>Are you a Property Manager?</a>
    <a class="nav-item" href="#"><svg viewBox="0 0 20 20" width="20"><rect width="20" height="20" rx="4" fill="#4e4c4d"/><path d="M6 5c-1 1 0 5 4 8s6 2 6 1l-2-2-2 1c-1-1-3-2-3-4l1-1-2-3z" fill="#fff"/></svg>Contact Us</a>
  </nav>
</header>

<section class="hero" role="img" aria-label="Aerial photo of a neighbourhood of houses with red tiled roofs">
  <div class="finder">
    <h1>FIND YOUR LOCAL PROPERTY MANAGER</h1>
    <span class="field-label" style="left:32px">Select Your Property Type :</span>
    <span class="field-label" style="left:456px">In Zipcode :</span>
    <div class="select">Single Home or Condo ($300 to $500K)
      <span class="select-btn"><svg width="12" height="12" viewBox="0 0 12 12"><path d="M2 2l4 4 4-4M2 6l4 4 4-4" fill="none" stroke="#fff" stroke-width="1.8"/></svg></span></div>
    <div class="zip"></div>
    <div class="search-btn"><svg width="16" height="16" viewBox="0 0 16 16"><circle cx="6.5" cy="6.5" r="4.5" fill="none" stroke="#fff" stroke-width="2.4"/><path d="M10 10l4.5 4.5" stroke="#fff" stroke-width="2.8"/></svg>Search</div>
    <p>Search our directory to find experienced and professional property management companies that meet your needs.</p>
  </div>
</section>

<h2 class="steps-title">To Find Property Management Companies Near You</h2>

<div class="step" style="left:46px">
  <svg viewBox="0 0 80 72" width="80"><path d="M32 4 2 32h8v24h16V40h12v16h8V32h8z" fill="#4e4c4d"/><rect x="44" y="8" width="8" height="14" fill="#4e4c4d"/><rect x="47" y="44" width="28" height="24" rx="4" fill="#fff" stroke="#fbc30a" stroke-width="3"/><path d="M53 55l6 6 16-16" fill="none" stroke="#fbc30a" stroke-width="5"/></svg>
  Select your property type and zipcode</div>
<div class="step" style="left:427px">
  <svg viewBox="0 0 82 72" width="82"><rect x="1" y="3" width="70" height="56" rx="5" fill="#4e4c4d"/><rect x="7" y="15" width="58" height="38" fill="#fff"/><g fill="#4e4c4d"><rect x="11" y="20" width="4" height="4"/><rect x="18" y="20" width="44" height="4"/><rect x="11" y="28" width="4" height="4"/><rect x="18" y="28" width="44" height="4"/><rect x="11" y="36" width="4" height="4"/><rect x="18" y="36" width="44" height="4"/><rect x="11" y="44" width="4" height="4"/><rect x="18" y="44" width="44" height="4"/></g><circle cx="67" cy="49" r="6" fill="#fbc30a"/><path d="M54 72c0-9 6-14 13-14s13 5 13 14z" fill="#fbc30a"/></svg>
  Review property manager listings in your area</div>
<div class="step" style="left:808px">
  <svg viewBox="0 0 72 72" width="72"><path d="M2 2h30l16 16v50H2z" fill="#4e4c4d"/><path d="M32 2v16h16" fill="#888"/><g fill="#fff"><rect x="9" y="26" width="30" height="4"/><rect x="9" y="34" width="30" height="4"/><rect x="9" y="42" width="22" height="4"/></g><circle cx="48" cy="52" r="5" fill="#fbc30a"/><circle cx="64" cy="52" r="5" fill="#fbc30a"/><circle cx="56" cy="58" r="6" fill="#fbc30a"/><path d="M40 70c0-7 7-10 16-10s16 3 16 10z" fill="#fbc30a"/></svg>
  Select and compare property managers</div>

<section class="info-box" style="left:52px">
  <h2>Are you a Property Manager?</h2>
  <p>Join our real estate property management company network. Let us help you find leads of property owners seeking to rent their homes.</p>
  <a class="learn-btn" href="#">Learn More</a>
</section>
<section class="info-box" style="left:622px">
  <h2>What You have to choose Us?</h2>
  <ul class="reasons">
    <li><svg width="18" height="16" viewBox="0 0 18 16"><path d="M1 6h9V1l7 7-7 7v-5H1z" fill="#4e4c4d"/></svg>Making renting Your home an easy, stress-free experience.</li>
    <li><svg width="18" height="16" viewBox="0 0 18 16"><path d="M1 6h9V1l7 7-7 7v-5H1z" fill="#4e4c4d"/></svg>Connecting property owners with property managers.</li>
    <li><svg width="18" height="16" viewBox="0 0 18 16"><path d="M1 6h9V1l7 7-7 7v-5H1z" fill="#4e4c4d"/></svg>Providing property management solutions, simplified.</li>
  </ul>
</section>

<footer class="site-footer">
  <span>Copyright © 2014, Venlox, All Rights Reserved</span>
  <span class="footer-links"><a href="#">Are you a Property Manager?</a><span>|</span><a href="#">About Us</a><span>|</span><a href="#">Contact Us</a><span>|</span><a href="#">Terms of Use</a><span>|</span><a href="#">Privacy Policy</a><span>|</span><a href="#">Site Map</a></span>
</footer>
</body>
</html>
```